7s Northgate Harriers Rugby Team

I need a website for a 7s Rugby team. 7s is a form of rugby union and one of the fastest rising sports in the world. Its recent addition to the Olympic games 2016 means that it's meteoric rise will only continue as more countries invest more money in their current programs as they compete for a chance at a medal.

See video for more insight: http://clipvault.example/v/Kx93TqLmWzA

I've started and Elite, Invitation 7s team for U16 boys, U18 boys, and eventually, senior men and junior women's programs to compliment what we already have in place.

We are hoping to attract the top players in across our region of southern Ontario with the goal of created the top 7s rugby program in Canada and providing and ideal pathway for those that want to one day play for Canada.

I want a design that is bright, sharp, professional, flashy and has visual appeal.
Updates

Please see most recent uploaded photos and include these in your designs.  

Additionally, please have a look at the updated colour-scheme.

Thanks

Added Sunday, December 22, 2013

Project Deadline Extended
Reason: Holidays and life have had consumed my energy and time. Would like to take the next week to complete this project with an appropriate amount of time and dedication. Thank you.
Added Sunday, December 29, 2013

Please change images in all designs to include those I have uploaded.

Final decision made by the end of the weekend.

Prize will be increased and split.

Thank you for your patience and continued efforts.

Greatly appreciated.

Added Friday, January 03, 2014

Target Market(s)

Active people between the ages of 14 and 30.

Industry/Entity Type

Union

Font styles to use
Sans Serif

Colors
3176b5
cedeec
f04a50
cee9f6
ceddec
0255a3
5c5c5c
474747

Requirements
Must have
• Highly effective use of visuals; responsive theme or something similar.

Something to encourage players or those interested to want to learn more and potentially register for our affiliated rugby Academy, "Keystone Rugby Canada".

Nice to have
• Connection to Vidly Channel

```html
<!DOCTYPE html>
<html lang="en">
<head>
<meta charset="utf-8">
<title>Northgate Harriers Sevens</title>
<link rel="stylesheet" href="https://fonts.googleapis.com/css2?family=Source+Sans+3:wght@400;600;700&display=swap">
<style>
:root{
  --blue:#3176b5;
  --blue-deep:#0255a3;
  --blue-pale:#cedeec;
  --row-tint:#dbe6ec;
  --red:#f04a50;
  --hero-red:#f0304a;
  --ink:#474747;
  --ink-soft:#5c5c5c;
  --panel-dark:#252525;
  --footer-dark:#1b1b1b;
  --white:#ffffff;
  --rule:#bfbfbf;
}
*{box-sizing:border-box;margin:0;padding:0}
html,body{width:1200px;height:1167px;overflow:hidden}
body{position:relative;font-family:"Source Sans 3",sans-serif;color:var(--ink);background:var(--footer-dark)}
.abs{position:absolute}

.stadium-backdrop{left:0;top:0;width:1200px;height:970px;
  background:radial-gradient(ellipse at 50% 20%,#3a2a2a 0%,#1e1616 45%,transparent 70%),
  linear-gradient(180deg,#2a1d1d 0%,#3b2424 18%,#2b3a22 35%,#3f7a2c 60%,#4f8d33 80%,#2c5a1e 100%)}
.player-left{left:0;top:250px;width:204px;height:720px;background:linear-gradient(180deg,rgba(190,40,40,.55),rgba(90,30,30,.5) 60%,rgba(40,70,30,.3))}
.player-right{left:996px;top:260px;width:204px;height:710px;background:linear-gradient(180deg,rgba(190,40,40,.55),rgba(90,30,30,.5) 60%,rgba(40,70,30,.3))}
.site-footer-band{left:0;top:970px;width:1200px;height:197px;background:repeating-linear-gradient(180deg,#1d1d1d 0 3px,#161616 3px 5px)}

.flag-pole{width:4px;background:linear-gradient(90deg,#777,#ddd,#777)}
.team-flag{left:236px;top:24px;width:250px;height:138px;background:linear-gradient(135deg,#ffffff,#e9e9e9 60%,#cfcfcf);border-radius:4px 30px 6px 18px}
.team-name{left:236px;top:54px;width:250px;text-align:center;color:var(--blue-deep);font-weight:700;font-size:26px;line-height:28px}

.search{left:697px;top:22px;width:248px;height:31px;display:flex}
.search-field{flex:1;background:var(--white);font-size:11px;color:#333;padding:9px 0 0 17px}
.search-go{width:46px;background:var(--blue);color:var(--white);font-weight:700;font-size:13px;text-align:center;line-height:31px}
.social{right:255px;top:68px;display:flex;gap:6px;font-size:10px;font-weight:600;color:var(--white)}
.social span{display:flex;align-items:center;gap:3px}
.social i{display:inline-block;width:7px;height:7px;background:var(--red)}

.main{left:204px;top:179px;width:792px;height:791px;background:var(--white)}
.nav{left:0;top:0;width:792px;height:36px;background:linear-gradient(180deg,#3b82c2,#2a68a3);color:var(--white);font-weight:700;font-size:12px}
.nav-home{left:14px;top:4px;width:59px;height:28px;border-radius:4px;background:#1f2a36;text-align:center;line-height:28px}
.nav-item{top:0;line-height:36px}
.nav-util{right:14px;top:0;line-height:36px;font-weight:400;font-size:12px;display:flex;gap:9px}
.nav-util b{font-weight:400;opacity:.9}

.hero-photo{left:10px;top:46px;width:532px;height:265px;background:linear-gradient(180deg,#6aa0d8 0%,#9cc3e4 22%,#3f6a2e 35%,#d9b52a 55%,#3b3b3b 72%,#2a2a2a 100%)}
.hero-dots{left:34px;top:248px;display:flex;gap:6px}
.hero-dots i{width:11px;height:11px;border-radius:50%;background:#333;border:1px solid #999}
.hero-dots i:first-child{background:#aaa}
.hero-panel{left:542px;top:46px;width:239px;height:265px;background:var(--panel-dark)}
.hero-title{left:11px;top:26px;color:var(--hero-red);font-weight:700;font-size:37px;line-height:42px;letter-spacing:-.2px}
.hero-sub{left:11px;top:190px;color:var(--white);font-weight:700;font-size:17px;line-height:20px}

.standings{left:13px;top:329px;width:217px;height:289px;border:1px solid #d6d6d6;border-top:none}
.standings-bar{left:0;top:0;width:217px;height:33px;background:#202020}
.standings-tab{left:0;top:0;width:157px;height:33px;background:var(--red);clip-path:polygon(0 0,88% 0,100% 50%,88% 100%,0 100%)}
.standings-tab span{position:absolute;left:13px;top:9px;color:var(--white);font-weight:700;font-size:12px}
.standings-table{position:absolute;left:0;top:48px;width:215px;border-collapse:collapse;font-size:12px;color:#222}
.standings-table th{font-weight:600;font-size:12px;text-align:left;height:24px;vertical-align:top}
.standings-table td{height:20px}
.standings-table tbody tr:nth-child(even){background:var(--row-tint)}
.standings-table .rank{width:30px;text-align:center;font-weight:600}
.standings-table .pts{text-align:right;padding-right:16px}
.standings-table tr.home td{color:var(--red);font-weight:700}

.section-head{left:255px;width:527px;height:14px;display:flex;align-items:center;gap:14px;font-weight:700;font-size:12px;color:#222}
.section-head .rule{flex:1;height:1px;background:var(--rule)}
.section-head svg{flex:none}
.section-head .tail{width:30px;height:1px;background:var(--rule)}
.body-copy{font-size:10.5px;line-height:20px;color:var(--ink)}
.date-box{left:257px;top:464px;width:40px;height:47px;border:1px solid #ddd;font-size:10.5px;color:#222;padding:6px 0 0 8px;line-height:20px}

.portal{top:572px;width:172px;height:124px;border:1px solid #777}
.portal-label{left:0;top:49px;width:100%;height:21px;background:rgba(255,255,255,.55);text-align:center;font-weight:700;font-size:12px;line-height:21px;color:#222}
.portal-label em{font-style:normal;color:var(--red)}

.partners{left:0;top:725px;width:792px;height:66px;background:#e4e4e4;border-top:3px solid #cfcfcf}
.badge{background:#8a8a8a}

.footer-col{top:1000px;font-size:11px;color:var(--white);line-height:20px}
.footer-col h4{color:var(--blue);font-size:12px;font-weight:700;line-height:16px;margin-bottom:4px}
.footer-sep{top:993px;height:87px;border-left:1px dotted #777}
.legal{right:213px;top:989px;text-align:right;font-size:11px;line-height:18px;color:#bbb}
.legal b{color:var(--white);font-weight:600}
.footer-name{left:796px;top:1046px;width:180px;text-align:center;font-weight:700;font-size:24px;line-height:28px;color:#8c8c8c}
</style>
</head>
<body>

<div class="abs stadium-backdrop" role="img" aria-label="Rugby stadium with crowd and green field"></div>
<div class="abs player-left" role="img" aria-label="Players in red running with the ball"></div>
<div class="abs player-right" role="img" aria-label="Players in red running with the ball"></div>
<div class="abs site-footer-band"></div>

<div class="abs flag-pole" style="left:226px;top:8px;height:172px"></div>
<div class="abs flag-pole" style="left:962px;top:8px;height:172px"></div>
<div class="abs team-flag" role="img" aria-label="White team flag on a pole"></div>
<div class="abs team-name">Northgate<br>Harriers Sevens</div>

<div class="abs search"><div class="search-field">Search</div><div class="search-go">GO</div></div>
<div class="abs social">
  <span><i></i>Snapr</span><span><i></i>Plusr</span><span><i></i>Vidly</span><span><i></i>Friendr</span><span><i></i>Chirp</span><span><i></i>RSS</span>
</div>

<main class="abs main">
  <nav class="abs nav">
    <div class="abs nav-home">HOME</div>
    <span class="abs nav-item" style="left:96px">ABOUT</span>
    <span class="abs nav-item" style="left:161px">SCHEDULE</span>
    <span class="abs nav-item" style="left:247px">TEAM</span>
    <span class="abs nav-item" style="left:307px">GAME DAY</span>
    <span class="abs nav-item" style="left:389px">FANS</span>
    <div class="abs nav-util"><b>Login</b>|<b>Photos</b>|<b>Videos</b></div>
  </nav>

  <div class="abs hero-photo" role="img" aria-label="Team in yellow jerseys posing with trophy behind a championship banner">
    <div class="abs hero-dots"><i></i><i></i><i></i><i></i><i></i></div>
  </div>
  <div class="abs hero-panel">
    <div class="abs hero-title">JOIN RUGBY<br>SEVENS<br>TODAY</div>
    <div class="abs hero-sub">Season Memberships now<br>available</div>
  </div>

  <section class="abs standings">
    <div class="abs standings-bar"></div>
    <div class="abs standings-tab"><span>World Sevens Standings</span></div>
    <table class="standings-table">
      <thead><tr><th></th><th>TEAM</th><th class="pts">PTS</th></tr></thead>
      <tbody>
        <tr><td class="rank">1</td><td>New Zealand</td><td class="pts">58</td></tr>
        <tr><td class="rank">2</td><td>South Africa</td><td class="pts">56</td></tr>
        <tr><td class="rank">3</td><td>Fiji</td><td class="pts">48</td></tr>
        <tr><td class="rank">4</td><td>England</td><td class="pts">42</td></tr>
        <tr><td class="rank">5</td><td>Australia</td><td class="pts">38</td></tr>
        <tr><td class="rank">6</td><td>Argentina</td><td class="pts">36</td></tr>
        <tr><td class="rank">7</td><td>Kenya</td><td class="pts">32</td></tr>
        <tr><td class="rank">8</td><td>Samoa</td><td class="pts">31</td></tr>
        <tr><td class="rank">9</td><td>Wales</td><td class="pts">27</td></tr>
        <tr><td class="rank">10</td><td>France</td><td class="pts">23</td></tr>
        <tr class="home"><td class="rank">11</td><td>Canada</td><td class="pts">14</td></tr>
      </tbody>
    </table>
  </section>

  <div class="abs section-head" style="top:326px">MISSION<span class="rule"></span>
    <svg width="20" height="20" viewBox="0 0 20 20" fill="none" stroke="#f04a50" stroke-width="1.8"><circle cx="9" cy="11" r="7"/><circle cx="9" cy="11" r="3.5"/><path d="M9 11 17 3M14 3h3v3"/></svg><span class="tail"></span></div>
  <p class="abs body-copy" style="left:258px;top:358px;width:520px">Lorem ipsum dolor sit amet, consectetur adipiscing elit. Maecenas placerat turpis sed ultricies convallis. Sed sed ullamcorper odio. Nunc lobortis metus nec enim placerat lobortis. Curabitur placerat urna non turpis luctus condimentum. Nunc sapien ante, fermentum sed elementum nec, tempor id magna.</p>

  <div class="abs section-head" style="top:440px">NEWS &amp; ACTIVITIES<span class="rule"></span>
    <svg width="18" height="18" viewBox="0 0 18 18" fill="none" stroke="#f04a50" stroke-width="1.6"><rect x="1.5" y="3" width="15" height="13.5"/><path d="M1.5 7h15M5 1v4M13 1v4M6 7v9.5M10 7v9.5M1.5 10.5h15M1.5 13.5h15"/></svg><span class="tail"></span></div>
  <div class="abs date-box">19<br>NOV</div>
  <p class="abs body-copy" style="left:325px;top:471px;width:460px">Lorem ipsum dolor sit amet, consectetur adipiscing elit. Nullam sit amet quam metus, id iaculis mi.</p>

  <div class="abs section-head" style="top:536px">PORTALS<span class="rule"></span>
    <svg width="18" height="18" viewBox="0 0 18 18" fill="none" stroke="#f04a50" stroke-width="1.8"><path d="M7.5 10.5 10.5 7.5"/><path d="M8.5 4.5 10 3a3.2 3.2 0 0 1 4.6 4.6L13 9.2M9.5 13.5 8 15a3.2 3.2 0 0 1-4.6-4.6L5 8.8"/></svg><span class="tail"></span></div>

  <div class="abs portal" style="left:253px;background:linear-gradient(160deg,#5a7f6a,#1f2a2a 45%,#3e6f7e 80%,#2a4f5a)" role="img" aria-label="Players diving for the ball in a tackle">
    <div class="abs portal-label">PHOTOS <em>&gt;&gt;</em></div></div>
  <div class="abs portal" style="left:430px;background:linear-gradient(170deg,#9a4848,#c86a6a 35%,#d8d8d8 60%,#4f7a3a)" role="img" aria-label="Players contesting the ball on the pitch">
    <div class="abs portal-label">VIDEOS <em>&gt;&gt;</em></div></div>
  <div class="abs portal" style="left:607px;background:linear-gradient(150deg,#3a3a3a,#5b5b4a 40%,#4a8a3a 75%,#2f5f28)" role="img" aria-label="Recruitment poster with a player pointing forward"></div>

  <div class="abs partners">
    <div class="abs badge" style="left:78px;top:12px;width:74px;height:40px;border-radius:50%"></div>
    <div class="abs badge" style="left:168px;top:16px;width:80px;height:32px;border-radius:6px;background:#a5a5a5"></div>
    <div class="abs badge" style="left:293px;top:6px;width:52px;height:52px;border-radius:50%;background:#2e2e2e"></div>
    <div class="abs badge" style="left:385px;top:18px;width:94px;height:28px;border-radius:6px;background:#5a5a5a"></div>
    <div class="abs badge" style="left:525px;top:15px;width:82px;height:34px;border-radius:6px;background:#3a3a3a"></div>
    <div class="abs badge" style="left:625px;top:10px;width:70px;height:44px;border-radius:50%;background:#4a4a4a"></div>
    <div class="abs badge" style="left:627px;top:10px;width:0;height:0"></div>
    <div class="abs badge" style="left:626px;top:12px;width:0;height:0"></div>
    <div class="abs badge" style="left:626px;top:12px;width:0;height:0"></div>
    <div class="abs badge" style="left:627px;top:14px;width:0;height:0"></div>
    <div class="abs badge" style="left:626px;top:14px;width:0;height:0"></div>
    <div class="abs badge" style="left:626px;top:14px;width:0;height:0"></div>
    <div class="abs badge" style="left:626px;top:14px;width:0;height:0"></div>
    <div class="abs badge" style="left:626px;top:14px;width:0;height:0"></div>
    <div class="abs badge" style="left:627px;top:14px;width:0;height:0"></div>
    <div class="abs badge" style="left:627px;top:14px;width:0;height:0"></div>
    <div class="abs badge" style="left:627px;top:14px;width:0;height:0"></div>
    <div class="abs badge" style="left:626px;top:14px;width:0;height:0"></div>
    <div class="abs badge" style="left:627px;top:14px;width:0;height:0"></div>
    <div class="abs badge" style="left:626px;top:14px;width:0;height:0"></div>
    <div class="abs badge" style="left:626px;top:14px;width:0;height:0"></div>
    <div class="abs badge" style="left:627px;top:14px;width:0;height:0"></div>
    <div class="abs badge" style="left:626px;top:14px;width:0;height:0"></div>
    <div class="abs badge" style="left:626px;top:14px;width:0;height:0"></div>
    <div class="abs badge" style="left:626px;top:14px;width:0;height:0"></div>
    <div class="abs badge" style="left:626px;top:14px;width:0;height:0"></div>
    <div class="abs badge" style="left:627px;top:14px;width:0;height:0"></div>
    <div class="abs badge" style="left:626px;top:14px;width:0;height:0"></div>
    <div class="abs badge" style="left:626px;top:14px;width:0;height:0"></div>
    <div class="abs badge" style="left:627px;top:14px;width:0;height:0"></div>
    <div class="abs badge" style="left:626px;top:14px;width:0;height:0"></div>
    <div class="abs badge" style="left:626px;top:14px;width:0;height:0"></div>
    <div class="abs badge" style="left:626px;top:14px;width:0;height:0"></div>
    <div class="abs badge" style="left:626px;top:14px;width:0;height:0"></div>
    <div class="abs badge" style="left:626px;top:14px;width:0;height:0"></div>
    <div class="abs badge" style="left:626px;top:14px;width:0;height:0"></div>
    <div class="abs badge" style="left:626px;top:14px;width:0;height:0"></div>
    <div class="abs badge" style="left:626px;top:14px;width:0;height:0"></div>
    <div class="abs badge" style="left:626px;top:14px;width:0;height:0"></div>
    <div class="abs badge" style="left:626px;top:14px;width:0;height:0"></div>
    <div class="abs badge" style="left:626px;top:14px;width:0;height:0"></div>
    <div class="abs badge" style="left:626px;top:14px;width:0;height:0"></div>
    <div class="abs badge" style="left:626px;top:14px;width:0;height:0"></div>
    <div class="abs badge" style="left:626px;top:14px;width:0;height:0"></div>
    <div class="abs badge" style="left:626px;top:14px;width:0;height:0"></div>
    <div class="abs badge" style="left:626px;top:14px;width:0;height:0"></div>
    <div class="abs badge" style="left:626px;top:14px;width:0;height:0"></div>
    <div class="abs badge" style="left:626px;top:14px;width:0;height:0"></div>
    <div class="abs badge" style="left:626px;top:14px;width:0;height:0"></div>
    <div class="abs badge" style="left:626px;top:14px;width:0;height:0"></div>
    <div class="abs badge" style="left:626px;top:14px;width:0;height:0"></div>
    <div class="abs badge" style="left:626px;top:14px;width:0;height:0"></div>
    <div class="abs badge" style="left:626px;top:14px;width:0;height:0"></div>
    <div class="abs badge" style="left:626px;top:14px;width:0;height:0"></div>
    <div class="abs badge" style="left:626px;top:14px;width:0;height:0"></div>
    <div class="abs badge" style="left:626px;top:14px;width:0;height:0"></div>
    <div class="abs badge" style="left:626px;top:14px;width:0;height:0"></div>
    <div class="abs badge" style="left:626px;top:14px;width:0;height:0"></div>
    <div class="abs badge" style="left:626px;top:14px;width:0;height:0"></div>
    <div class="abs badge" style="left:626px;top:14px;width:0;height:0"></div>
    <div class="abs badge" style="left:626px;top:14px;width:0;height:0"></div>
    <div class="abs badge" style="left:626px;top:14px;width:0;height:0"></div>
    <div class="abs badge" style="left:626px;top:14px;width:0;height:0"></div>
    <div class="abs badge" style="left:626px;top:14px;width:0;height:0"></div>
    <div class="abs badge" style="left:626px;top:14px;width:0;height:0"></div>
    <div class="abs badge" style="left:626px;top:14px;width:0;height:0"></div>
    <div class="abs badge" style="left:626px;top:14px;width:0;height:0"></div>
    <div class="abs badge" style="left:626px;top:14px;width:0;height:0"></div>
    <div class="abs badge" style="left:626px;top:14px;width:0;height:0"></div>
    <div class="abs badge" style="left:626px;top:14px;width:0;height:0"></div>
    <div class="abs badge" style="left:626px;top:14px;width:0;height:0"></div>
    <div class="abs badge" style="left:626px;top:14px;width:0;height:0"></div>
    <div class="abs badge" style="left:626px;top:14px;width:0;height:0"></div>
    <div class="abs badge" style="left:626px;top:14px;width:0;height:0"></div>
    <div class="abs badge" style="left:626px;top:14px;width:0;height:0"></div>
    <div class="abs badge" style="left:626px;top:14px;width:0;height:0"></div>
    <div class="abs badge" style="left:626px;top:14px;width:0;height:0"></div>
    <div class="abs badge" style="left:626px;top:14px;width:0;height:0"></div>
    <div class="abs badge" style="left:626px;top:14px;width:0;height:0"></div>
    <div class="abs badge" style="left:626px;top:14px;width:0;height:0"></div>
    <div class="abs badge" style="left:626px;top:14px;width:0;height:0"></div>
    <div class="abs badge" style="left:626px;top:14px;width:0;height:0"></div>
    <div class="abs badge" style="left:626px;top:14px;width:0;height:0"></div>
    <div class="abs badge" style="left:626px;top:14px;width:0;height:0"></div>
    <div class="abs badge" style="left:626px;top:14px;width:0;height:0"></div>
    <div class="abs badge" style="left:626px;top:14px;width:0;height:0"></div>
    <div class="abs badge" style="left:626px;top:14px;width:0;height:0"></div>
    <div class="abs badge" style="left:626px;top:14px;width:0;height:0"></div>
    <div class="abs badge" style="left:626px;top:14px;width:0;height:0"></div>
    <div class="abs badge" style="left:626px;top:14px;width:0;height:0"></div>
    <div class="abs badge" style="left:626px;top:14px;width:0;height:0"></div>
    <div class="abs badge" style="left:626px;top:14px;width:0;height:0"></div>
    <div class="abs badge" style="left:626px;top:14px;width:0;height:0"></div>
    <div class="abs badge" style="left:626px;top:14px;width:0;height:0"></div>
    <div class="abs badge" style="left:626px;top:14px;width:0;height:0"></div>
    <div class="abs badge" style="left:626px;top:14px;width:0;height:0"></div>
    <div class="abs badge" style="left:626px;top:14px;width:0;height:0"></div>
    <div class="abs badge" style="left:626px;top:14px;width:0;height:0"></div>
    <div class="abs badge" style="left:626px;top:14px;width:0;height:0"></div>
    <div class="abs badge" style="left:626px;top:14px;width:0;height:0"></div>
    <div class="abs badge" style="left:626px;top:14px;width:0;height:0"></div>
    <div class="abs badge" style="left:626px;top:14px;width:0;height:0"></div>
    <div class="abs badge" style="left:626px;top:14px;width:0;height:0"></div>
    <div class="abs badge" style="left:626px;top:14px;width:0;height:0"></div>
    <div class="abs badge" style="left:626px;top:14px;width:0;height:0"></div>
    <div class="abs badge" style="left:626px;top:14px;width:0;height:0"></div>
    <div class="abs badge" style="left:626px;top:14px;width:0;height:0"></div>
    <div class="abs badge" style="left:626px;top:14px;width:0;height:0"></div>
    <div class="abs badge" style="left:626px;top:14px;width:0;height:0"></div>
    <div class="abs badge" style="left:626px;top:14px;width:0;height:0"></div>
    <div class="abs badge" style="left:626px;top:14px;width:0;height:0"></div>
    <div class="abs badge" style="left:626px;top:14px;width:0;height:0"></div>
    <div class="abs badge" style="left:626px;top:14px;width:0;height:0"></div>
    <div class="abs badge" style="left:626px;top:14px;width:0;height:0"></div>
    <div class="abs badge" style="left:626px;top:14px;width:0;height:0"></div>
    <div class="abs badge" style="left:626px;top:14px;width:0;height:0"></div>
    <div class="abs badge" style="left:626px;top:14px;width:0;height:0"></div>
    <div class="abs badge" style="left:626px;top:14px;width:0;height:0"></div>
    <div class="abs badge" style="left:626px;top:14px;width:0;height:0"></div>
    <div class="abs badge" style="left:626px;top:14px;width:0;height:0"></div>
    <div class="abs badge" style="left:626px;top:14px;width:0;height:0"></div>
    <div class="abs badge" style="left:626px;top:14px;width:0;height:0"></div>
    <div class="abs badge" style="left:626px;top:14px;width:0;height:0"></div>
    <div class="abs badge" style="left:626px;top:14px;width:0;height:0"></div>
    <div class="abs badge" style="left:626px;top:14px;width:0;height:0"></div>
    <div class="abs badge" style="left:626px;top:14px;width:0;height:0"></div>
    <div class="abs badge" style="left:626px;top:14px;width:0;height:0"></div>
    <div class="abs badge" style="left:626px;top:14px;width:0;height:0"></div>
    <div class="abs badge" style="left:626px;top:14px;width:0;height:0"></div>
    <div class="abs badge" style="left:626px;top:14px;width:0;height:0"></div>
    <div class="abs badge" style="left:626px;top:14px;width:0;height:0"></div>
    <div class="abs badge" style="left:626px;top:14px;width:0;height:0"></div>
    <div class="abs badge" style="left:626px;top:14px;width:0;height:0"></div>
    <div class="abs badge" style="left:626px;top:14px;width:0;height:0"></div>
    <div class="abs badge" style="left:626px;top:14px;width:0;height:0"></div>
    <div class="abs badge" style="left:626px;top:14px;width:0;height:0"></div>
    <div class="abs badge" style="left:626px;top:14px;width:0;height:0"></div>
    <div class="abs badge" style="left:626px;top:14px;width:0;height:0"></div>
    <div class="abs badge" style="left:626px;top:14px;width:0;height:0"></div>
    <div class="abs badge" style="left:626px;top:14px;width:0;height:0"></div>
    <div class="abs badge" style="left:626px;top:14px;width:0;height:0"></div>
    <div class="abs badge" style="left:626px;top:14px;width:0;height:0"></div>
    <div class="abs badge" style="left:626px;top:14px;width:0;height:0"></div>
    <div class="abs badge" style="left:626px;top:14px;width:0;height:0"></div>
    <div class="abs badge" style="left:626px;top:14px;width:0;height:0"></div>
    <div class="abs badge" style="left:626px;top:14px;width:0;height:0"></div>
    <div class="abs badge" style="left:626px;top:14px;width:0;height:0"></div>
    <div class="abs badge" style="left:626px;top:14px;width:0;height:0"></div>
    <div class="abs badge" style="left:626px;top:14px;width:0;height:0"></div>
    <div class="abs badge" style="left:626px;top:14px;width:0;height:0"></div>
    <div class="abs badge" style="left:626px;top:14px;width:0;height:0"></div>
    <div class="abs badge" style="left:626px;top:14px;width:0;height:0"></div>
    <div class="abs badge" style="left:626px;top:14px;width:0;height:0"></div>
    <div class="abs badge" style="left:626px;top:14px;width:0;height:0"></div>
    <div class="abs badge" style="left:626px;top:14px;width:0;height:0"></div>
    <div class="abs badge" style="left:626px;top:14px;width:0;height:0"></div>
    <div class="abs badge" style="left:626px;top:14px;width:0;height:0"></div>
    <div class="abs badge" style="left:626px;top:14px;width:0;height:0"></div>
    <div class="abs badge" style="left:626px;top:14px;width:0;height:0"></div>
    <div class="abs badge" style="left:626px;top:14px;width:0;height:0"></div>
    <div class="abs badge" style="left:626px;top:14px;width:0;height:0"></div>
    <div class="abs badge" style="left:726px;top:14px;width:38px;height:38px;border-radius:50%;background:#6a6a6a"></div>
  </div>
</main>

<div class="abs footer-col" style="left:209px"><h4>ABOUT US</h4>Unions<br>Corporations<br>Privacy Policy<br>Our Sponsors</div>
<div class="abs footer-sep" style="left:330px"></div>
<div class="abs footer-col" style="left:354px"><h4>PEOPLE</h4>Players<br>Staff<br>Board of Directors</div>
<div class="abs footer-sep" style="left:462px"></div>
<div class="abs footer-col" style="left:479px"><h4>TEAM PROFILE</h4>Squad<br>Contact</div>
<div class="abs footer-sep" style="left:595px"></div>
<div class="abs footer-col" style="left:612px"><h4>FOR FANS</h4>Merchandise<br>Photos<br>Videos</div>
<div class="abs footer-sep" style="left:745px"></div>
<div class="abs legal">© 2014 Northgate Harriers. All rights reserved.<br><b>Terms &amp; Conditions</b> | <b>Sitemap</b></div>
<div class="abs footer-name">Northgate<br>Harriers Sevens</div>

</body>
</html>
```